Quarry & Knowbright executive recruiting services

I started a pagevine website using an existing template and some of the original content is still on this UNpublished work in progress. I am an executive recruiter offering services to both Clients and Candidates in many sectors and using creative sourcing methodologies. I have 30+ years of business experience combined with my recruiting experience. I like the color teal and used it for the site I started. The tabs should be
About (me)
Services (for Clients and Candidates)
Industry Coverage
Recruiting Process (see attached flow chart)
Retained Agreement (see attached)
Personal Commitment
Testimonials
Content/articles/blogs etc
Contact
Updates

TO ALL DESIGNERS:
I have been granted a short extension to choose a design. Please resubmit designs using a new name TORLEN EXECUTIVE SEARCH. Pls feel free to alert me with any questions and of course, when the edits are made.

thank you

Priscilla

Target Market(s)

Executives from Director, VP, SVP and C-Suite

Industry/Entity Type

recruiting industry for finance, Human Resoures, Sales/Marketing, Innovation/Transformation , Information Technology, Entertainment/Media/Telecommunications, Healthcare/Life Sciences,HCIT/Biotech

Font styles to use
Sans Serif

Colors
0094D4
00A9DD
6FCCEA
C7EBF8
E9F6FB

Requirements
Must have
• way to contact me - add calendar sign up
Nice to have
• process flow for the recruiting process (see attached)
Should not have
• guarantees

```html
<!DOCTYPE html>
<html lang="en">
<head>
<meta charset="utf-8">
<title>Quarry &amp; Knowbright — Executive Recruiting</title>
<link href="https://fonts.googleapis.com/css2?family=Roboto:wght@400;500;700;900&display=swap" rel="stylesheet">
<style>
:root{
  --blue:#0094D4;
  --blue-2:#00A9DD;
  --blue-3:#6FCCEA;
  --blue-4:#C7EBF8;
  --blue-5:#E9F6FB;
  --ink:#141414;
  --text:#555;
  --footer:#222;
  --white:#fff;
}
*{margin:0;padding:0;box-sizing:border-box}
html,body{width:1200px;height:3504px;overflow:hidden}
body{position:relative;font-family:'Roboto',sans-serif;color:var(--ink);background:var(--white)}

/* header */
.site-header{position:absolute;left:0;top:0;width:1200px;height:90px;background:var(--white);z-index:3}
.brand{position:absolute;left:60px;top:-57px;width:230px;height:230px;border-radius:50%;background:var(--white);z-index:4}
.brand-name{position:absolute;left:0;width:230px;top:171px;text-align:center;font-size:12.5px;font-weight:700;letter-spacing:.4px;color:var(--ink)}
.main-nav{position:absolute;left:316px;top:37px;display:flex;gap:16.5px;font-size:13.5px;color:var(--ink)}
.btn-signup{position:absolute;left:1038px;top:28px;width:103px;height:36px;border-radius:18px;background:var(--blue);color:var(--white);font-size:14px;font-weight:500;display:flex;align-items:center;justify-content:center}

/* hero */
.hero{position:absolute;left:0;top:90px;width:1200px;height:644px;background:linear-gradient(90deg,#5d6670 0%,#8a8f93 30%,#b9a998 55%,#9e8a78 75%,#7b7b80 100%)}
.hero-shade{position:absolute;inset:0;background:linear-gradient(90deg,rgba(40,48,58,.55) 0%,rgba(40,48,58,.25) 45%,rgba(0,0,0,0) 70%)}
.hero-title{position:absolute;left:110px;top:206px;font-size:34.5px;line-height:41px;font-weight:700;color:var(--white);letter-spacing:.6px}
.hero-text{position:absolute;left:111px;top:307px;width:520px;font-size:16px;line-height:24px;color:var(--white);font-weight:500}
.btn{display:flex;align-items:center;justify-content:center;border-radius:24px;font-weight:500}
.hero-btn{position:absolute;left:111px;top:383px;width:170px;height:44px;background:var(--blue);color:var(--white);font-size:16.5px}

/* audience band */
.audience{position:absolute;top:734px;width:600px;height:243px;color:var(--white)}
.audience.clients{left:0;background:linear-gradient(90deg,#0a8fd0,var(--blue))}
.audience.candidates{left:600px;background:var(--blue-2)}
.aud-icon{position:absolute;left:110px;top:45px;width:71px;height:71px;border-radius:50%;background:var(--white)}
.aud-title{position:absolute;left:195px;top:40px;font-size:19.5px;font-weight:700;letter-spacing:.4px}
.aud-text{position:absolute;left:196px;top:75px;width:355px;font-size:13.2px;line-height:21.5px;text-align:justify}
.aud-btn{position:absolute;left:196px;top:164px;width:125px;height:34px;background:var(--white);color:var(--blue);font-size:13.5px;border-radius:17px}

/* about */
.about-photo-ring{position:absolute;left:110px;top:1055px;width:420px;height:420px;border-radius:50%;border:11px solid #d9d9d9;background:var(--white)}
.about-photo{position:absolute;left:16px;top:16px;width:366px;height:366px;border-radius:50%;background:radial-gradient(circle at 50% 40%,#e8d9cf 0%,#cdb8a8 45%,#8a7f78 100%)}
.section-title{font-size:32px;font-weight:700;letter-spacing:.6px;color:var(--ink)}
.about-title{position:absolute;left:604px;top:1073px}
.about-copy{position:absolute;left:600px;width:488px;font-size:13.2px;line-height:23px;color:var(--text);text-align:justify}
.about-btn{position:absolute;left:600px;top:1415px;width:125px;height:34px;background:var(--blue);color:var(--white);font-size:13.5px;border-radius:17px}

/* commitment */
.commitment{position:absolute;left:0;top:1548px;width:1200px;height:357px;background:radial-gradient(ellipse at 50% 50%,var(--blue-5) 0%,#dcf0f9 100%)}
.commitment-title{position:absolute;left:0;width:1200px;top:56px;text-align:center}
.commit-card{position:absolute;top:140px;width:185px;height:154px;background:var(--white);border-radius:3px;box-shadow:0 1px 4px rgba(0,0,0,.08);text-align:center}
.commit-card svg{position:absolute;left:64px;top:24px}
.commit-label{position:absolute;left:0;width:185px;top:95px;font-size:15px;line-height:18px;font-weight:500;color:var(--ink)}
.slider-arrow{position:absolute;top:205px}

/* process */
.process-title{position:absolute;left:0;width:1200px;top:1958px;text-align:center}
.process-graphic{position:absolute;left:110px;top:2030px;width:975px;height:600px;border-radius:300px;background:radial-gradient(ellipse at 50% 50%,var(--blue-4) 0%,var(--blue-3) 55%,var(--blue) 100%)}

/* sectors */
.sectors-title{position:absolute;left:0;width:1200px;top:2725px;text-align:center}
.sector{position:absolute;top:2800px;width:291px;height:336px}
.sector-label{position:absolute;left:0;width:100%;bottom:26px;text-align:center;font-size:18.5px;font-weight:700;color:var(--white)}

/* footer */
.site-footer{position:absolute;left:0;top:3136px;width:1200px;height:316px;background:var(--footer);color:var(--white)}
.foot-head{position:absolute;top:52px;font-size:18.5px;font-weight:700;letter-spacing:.2px}
.foot-rule{position:absolute;top:88px;width:66px;height:2px;background:var(--white)}
.foot-help{position:absolute;left:111px;top:126px;width:302px;font-size:15px;line-height:26px;text-align:justify;color:#eee}
.foot-divider{position:absolute;top:61px;width:1px;height:211px;background:#555}
.quick-links{position:absolute;left:570px;top:110px;list-style:none;font-size:11.8px;line-height:26px;color:#eee}
.contact-item{position:absolute;left:860px;display:flex;align-items:flex-start;gap:12px;font-size:12px;line-height:19px;color:#eee}
.contact-icon{width:24px;height:24px;border-radius:50%;background:#e6e6e6;flex:none;display:flex;align-items:center;justify-content:center}
.chat-bubble{position:absolute;left:1127px;top:245px}
.bottom-bar{position:absolute;left:0;top:3452px;width:1200px;height:52px;background:var(--blue);color:var(--white);font-size:13px}
.bottom-bar .copy{position:absolute;left:111px;top:17px}
.bottom-bar .copy span{text-decoration:underline}
.bottom-links{position:absolute;left:809px;top:17px;display:flex;gap:12px}
.bottom-code{position:absolute;left:1131px;top:18px;font-size:12px}
</style>
</head>
<body>

<header class="site-header">
  <nav class="main-nav">
    <span>Home</span><span>About</span><span>Services</span><span>Industry Coverage</span><span>Process</span><span>Retained Agreement</span><span>Commitment</span><span>blog</span><span>Contact</span>
  </nav>
  <div class="btn-signup">Sign Up</div>
</header>
<div class="brand">
  <div class="brand-name">QUARRY &amp; KNOWBRIGHT</div>
</div>

<section class="hero" role="img" aria-label="Photo of a smiling businesswoman in a bright office meeting with a colleague">
  <div class="hero-shade"></div>
  <h1 class="hero-title">QUARRY &amp; KNOWBRIGHT<br>FOR SOURCING SERVICES</h1>
  <p class="hero-text">Welcome to the Quarry &amp; Knowbright recruiting website! If you are looking to grow your team or change careers,</p>
  <div class="btn hero-btn">LEARN MORE</div>
</section>

<section class="audience clients">
  <div class="aud-icon">
    <svg width="71" height="71" viewBox="0 0 71 71" fill="none" stroke="#0094D4" stroke-width="2">
      <circle cx="27" cy="24" r="4"/><circle cx="36" cy="24" r="4"/><circle cx="45" cy="24" r="4"/>
      <path d="M21 37h29v-4a4 4 0 0 0-4-4H25a4 4 0 0 0-4 4z"/>
      <path d="M16 45l8-4h12l-3 5h-9M16 51l10 1 22-9"/>
    </svg>
  </div>
  <h2 class="aud-title">FOR CLIENTS</h2>
  <p class="aud-text">If you are a company and looking to grow or change your team, join the clients who have relied on me for their most senior and critical placements.</p>
  <div class="btn aud-btn">LEARN MORE</div>
</section>
<section class="audience candidates">
  <div class="aud-icon">
    <svg width="71" height="71" viewBox="0 0 71 71" fill="none" stroke="#00A9DD" stroke-width="2">
      <circle cx="33" cy="31" r="14"/><line x1="43" y1="41" x2="53" y2="51"/>
      <circle cx="33" cy="27" r="4"/><path d="M26 38a7 7 0 0 1 14 0"/>
    </svg>
  </div>
  <h2 class="aud-title">FOR CANDIDATES</h2>
  <p class="aud-text">You are critical to the recruiting process. The former candidates I've worked with find me refreshingly honest, responsive, and trustworthy.</p>
  <div class="btn aud-btn">LEARN MORE</div>
</section>

<section class="about">
  <div class="about-photo-ring">
    <div class="about-photo" role="img" aria-label="Portrait photo of a smiling recruiter in a striped blouse holding a clipboard"></div>
  </div>
  <h2 class="section-title about-title">A LITTLE MORE ABOUT ME</h2>
  <p class="about-copy" style="top:1138px">Most recently, I was a retained recruiter for a $1.5B digital transformation co. In the last two years alone, I used my “personal approach,” to place nearly 20 of their new Directors, VPs, SVPs and contributed to C-Suites search efforts.</p>
  <p class="about-copy" style="top:1219px">Earlier in my career, I built global business teams for Harborline Bank, Kestrel Advisory and Vantor Data and was part of the Meridian Ledger sales team. I've interviewed 1000s of professionals; hired and fired countless others; and managed global teams both onsite and offshore.</p>
  <p class="about-copy" style="top:1322px">I have an extensive research background which fuels my creative sourcing skills as I seek to find the “needle in the haystack” passive candidate who is not looking for a new role.</p>
  <div class="btn about-btn">LEARN MORE</div>
</section>

<section class="commitment">
  <h2 class="section-title commitment-title">MY PERSONAL COMMITMENT</h2>
  <svg class="slider-arrow" style="left:50px" width="16" height="26" viewBox="0 0 16 26"><path d="M12 3L3 13l9 10" fill="none" stroke="#222" stroke-width="2"/></svg>
  <svg class="slider-arrow" style="left:1134px" width="16" height="26" viewBox="0 0 16 26"><path d="M4 3l9 10-9 10" fill="none" stroke="#222" stroke-width="2"/></svg>

  <div class="commit-card" style="left:103px">
    <svg width="56" height="56" viewBox="0 0 56 56" fill="none" stroke="#0094D4" stroke-width="2"><path d="M14 18a9 9 0 0 1 17-5 8 8 0 0 1 13 6 7 7 0 0 1-2 13H14a7 7 0 0 1 0-14z"/><rect x="18" y="34" width="22" height="16" rx="2"/><line x1="18" y1="42" x2="40" y2="42"/><circle cx="14" cy="46" r="5"/></svg>
    <div class="commit-label">Dedicated service</div>
  </div>
  <div class="commit-card" style="left:305px">
    <svg width="56" height="56" viewBox="0 0 56 56" fill="none" stroke="#0094D4" stroke-width="2"><path d="M20 50V30l8-14c3 0 4 2 3 5l-2 7h12a3 3 0 0 1 3 4l-3 14a3 3 0 0 1-3 3z"/><rect x="11" y="30" width="9" height="20"/><path d="M8 14l2 4 4 1-3 3 1 4-4-2-4 2 1-4-3-3 4-1zM48 14l2 4 4 1-3 3 1 4-4-2-4 2 1-4-3-3 4-1zM28 2l2 4 4 1-3 3 1 4-4-2-4 2 1-4-3-3 4-1z"/></svg>
    <div class="commit-label">Customer satisfaction</div>
  </div>
  <div class="commit-card" style="left:506px">
    <svg width="56" height="56" viewBox="0 0 56 56" fill="none" stroke="#0094D4" stroke-width="2"><rect x="4" y="6" width="48" height="34" rx="2"/><line x1="4" y1="34" x2="52" y2="34"/><path d="M22 40l-2 10h16l-2-10M16 50h24"/><circle cx="28" cy="20" r="6"/><circle cx="28" cy="20" r="10" stroke-dasharray="3 3"/></svg>
    <div class="commit-label">Develop and maintain<br>trust</div>
  </div>
  <div class="commit-card" style="left:707px">
    <svg width="56" height="56" viewBox="0 0 56 56" fill="none" stroke="#0094D4" stroke-width="2"><circle cx="20" cy="22" r="10"/><path d="M4 52c0-10 7-16 16-16s16 6 16 16"/><path d="M14 22l4 4 8-8"/><path d="M36 6h16v12h-8l-5 4v-4h-3z"/></svg>
    <div class="commit-label">Adherance to strict<br>confidentiality</div>
  </div>
  <div class="commit-card" style="left:909px">
    <svg width="56" height="56" viewBox="0 0 56 56" fill="none" stroke="#0094D4" stroke-width="2"><rect x="4" y="6" width="48" height="36" rx="2"/><path d="M14 14l2 3 3 .5-2 2 .5 3-3.5-1.5-3 1.5.5-3-2-2 3-.5zM28 14l2 3 3 .5-2 2 .5 3-3.5-1.5-3 1.5.5-3-2-2 3-.5zM42 14l2 3 3 .5-2 2 .5 3-3.5-1.5-3 1.5.5-3-2-2 3-.5z"/><line x1="12" y1="30" x2="44" y2="30"/><line x1="12" y1="36" x2="34" y2="36"/><path d="M36 50l12-12 3 3-12 12h-3z"/></svg>
    <div class="commit-label">Provide detailed<br>feedback</div>
  </div>
</section>

<h2 class="section-title process-title">RECRUITING PROCESS</h2>
<div class="process-graphic" role="img" aria-label="Recruiting process infographic of eleven numbered steps: Candidate Consult, Sourcing, Candidate List Generation, Internal Team Review, Candidate Outreach, Present Candidates, Candidate Response Review, Interview Schedule, Candidate Interview Prep, Post-Interview Feedback, Offer Process"></div>

<h2 class="section-title sectors-title">SECTOR SPECIALTIES</h2>
<div class="sector" style="left:0;background:linear-gradient(160deg,#8f8a86,#4a4440 60%,#2e2a28)" role="img" aria-label="Photo of a hand using a calculator over financial papers">
  <div class="sector-label">Finance</div>
</div>
<div class="sector" style="left:303px;background:linear-gradient(160deg,#6d7480,#3c434f 60%,#262b33)" role="img" aria-label="Photo of two IT professionals working on a laptop in a server room">
  <div class="sector-label">Information Technology</div>
</div>
<div class="sector" style="left:605px;background:linear-gradient(160deg,#b7b4b0,#6e6a66 60%,#3a3836)" role="img" aria-label="Photo of a smiling doctor in a white coat holding a tablet">
  <div class="sector-label">Healthcare</div>
</div>
<div class="sector" style="left:909px;background:linear-gradient(160deg,#a7a29c,#5f5a55 60%,#35322f)" role="img" aria-label="Photo of a smiling HR professional in a light blazer">
  <div class="sector-label">Human Resources</div>
</div>

<footer class="site-footer">
  <h3 class="foot-head" style="left:111px">HOW MAY I HELP YOU?</h3>
  <div class="foot-rule" style="left:111px"></div>
  <p class="foot-help">Contact Q&amp;K to learn more about the recruiting services or to answer your questions. CONNECTING TALENTED PEOPLE WITH DYNAMIC OPPORTUNITIES AT EXCELENT COMPANIES</p>
  <div class="foot-divider" style="left:482px"></div>

  <h3 class="foot-head" style="left:565px">QUICK LINKS</h3>
  <ul class="quick-links">
    <li>Home</li><li>About Me</li><li>Services</li><li>Recruiting Process</li><li>Retained Agreement</li><li>Personal Commitment</li><li>Testimonials</li>
  </ul>
  <div class="foot-divider" style="left:774px"></div>

  <h3 class="foot-head" style="left:863px">CONTACT US</h3>
  <div class="contact-item" style="top:115px">
    <span class="contact-icon"><svg width="12" height="12" viewBox="0 0 12 12"><path d="M2.5 1l2 2-1 1.5a7 7 0 0 0 4 4L9 7.5l2 2-1.5 1.5C5 11 1 7 1 2.5z" fill="#222"/></svg></span>
    <span>917 555 0142</span>
  </div>
  <div class="contact-item" style="top:156px">
    <span class="contact-icon"><svg width="12" height="10" viewBox="0 0 12 10"><rect x="0" y="0" width="12" height="10" rx="1" fill="#222"/><path d="M1 1.5l5 4 5-4" fill="none" stroke="#e6e6e6" stroke-width="1.2"/></svg></span>
    <span>priscilla@quarryknowbright.com</span>
  </div>
  <div class="contact-item" style="top:194px">
    <span class="contact-icon"><svg width="10" height="13" viewBox="0 0 10 13"><path d="M5 0a5 5 0 0 1 5 5c0 3.5-5 8-5 8S0 8.5 0 5a5 5 0 0 1 5-5z" fill="#222"/><circle cx="5" cy="5" r="1.8" fill="#e6e6e6"/></svg></span>
    <span>123, Lorem ipsum dolor sit amet,<br>adipiscing elit, sed do</span>
  </div>
  <div class="contact-item" style="top:252px">
    <span class="contact-icon"><svg width="12" height="12" viewBox="0 0 12 12"><rect x="3" y="0" width="6" height="3" fill="#222"/><rect x="0" y="3" width="12" height="6" rx="1" fill="#222"/><rect x="3" y="7" width="6" height="5" fill="#222" stroke="#e6e6e6" stroke-width=".8"/></svg></span>
    <span>123-456-7890</span>
  </div>

  <svg class="chat-bubble" width="42" height="42" viewBox="0 0 42 42"><circle cx="21" cy="21" r="21" fill="#0094D4"/><path d="M12 20c0-5 4-8 9-8s9 3 9 8-4 8-9 8c-1.5 0-3-.3-4-.8L12 29l1.3-3.5C12.5 24 12 22 12 20z" fill="#fff"/><circle cx="17" cy="20" r="1.3" fill="#0094D4"/><circle cx="21" cy="20" r="1.3" fill="#0094D4"/><circle cx="25" cy="20" r="1.3" fill="#0094D4"/></svg>
</footer>

<div class="bottom-bar">
  <div class="copy">Copyright© 2023 <span>Quarry &amp; Knowbright</span> | All Rights Reserved</div>
  <div class="bottom-links"><span>Specifications</span><span>|</span><span>Site Map</span><span>|</span><span>Privacy Policy</span></div>
  <div class="bottom-code">C47</div>
</div>

</body>
</html>
```